Flyer LMTG

Everyone deserves true happiness.
Real Food is the answer to:
A body you love
Reverting illnesses
Healthy digestion
Stable blood sugar
Emotions in control
Blasting energy
Sound sleep
REAL food + water + exercise + Laughter =
“HIGH QUALITY OF LIFE “
EASY, right?
Challenging: certainly
Changing habits: reluctance in sight!
WE’RE OFFER TO:
1. Study YOUR unique body composition, food cravings, blockages, illnesses, and personality!
2. Introduce you to new Food
3. customized wellness plan with follow ups
4. meditation,cooking, and fitness classes as well as wellness workshops
5. New friends with high aspirations
LOGO
Contact info
Please visit our web address to see our design style and colors: www.larkmosstideglow.net
Target Market(s)
people who want to be more healthy
Industry/Entity Type
Fitness
Requirements
Must have
- beautiful pictures of fresh food (main picture) and maybe a few more small pictures reflecting
exercise
healthy living
meditation
Nice to have
- look is crucial. recall some of the color or colors from my logo to have a theme

```html
<!DOCTYPE html>
<html lang="en">
<head>
<meta charset="utf-8">
<title>Flyer LMTG</title>
<link href="https://fonts.googleapis.com/css2?family=Cabin:wght@400;500;600;700&family=Parisienne&display=swap" rel="stylesheet">
<style>
  :root {
    --orange: #e8702a;
    --orange-deep: #f08a2c;
    --green: #2e8a2f;
    --green-dark: #256f27;
    --ink: #1d1d1b;
    --navy: #1f2f6b;
    --cream: #fff3cf;
    --cream-deep: #fde6a6;
    --mint: #e6f3d2;
    --mint-deep: #cfe7ad;
    --peach: #fde0a8;
    --peach-deep: #f7a54a;
    --veil: rgba(255, 250, 235, 0.6);
    --white: #ffffff;
  }
  * { box-sizing: border-box; margin: 0; padding: 0; }
  html, body { width: 1200px; height: 849px; overflow: hidden; background: #f4f1ea; }
  body { font-family: "Cabin", sans-serif; color: var(--ink); }

  .flyer { position: relative; width: 1200px; height: 849px; display: flex; }
  .panel { position: relative; width: 400px; height: 849px; overflow: hidden; }

  /* left panel */
  .panel--intro { background: repeating-linear-gradient(90deg, var(--cream) 0 14px, #fff6da 14px 28px); }
  .brand-head {
    position: absolute; left: 0; top: 0; width: 400px; height: 124px;
    background: var(--white); display: flex; align-items: center; padding-left: 18px; gap: 12px;
    border-bottom: 3px solid var(--cream-deep);
  }
  .brand-dot { width: 64px; height: 64px; border-radius: 50%; background: var(--green); flex: none; }
  .brand-name { font-size: 32px; font-weight: 500; color: var(--green-dark); line-height: 1; }
  .brand-tag { font-size: 9.5px; font-weight: 600; color: var(--green-dark); letter-spacing: 0.5px; margin-top: 5px; }
  .motto { position: absolute; left: 0; top: 118px; width: 400px; height: 70px; }
  .motto text { font-family: "Parisienne", cursive; font-size: 24px; fill: var(--green); }
  .answer-title { position: absolute; left: 0; top: 212px; width: 400px; text-align: center; font-size: 25px; font-weight: 500; }
  .answer-title .accent { color: var(--orange); }
  .benefits { position: absolute; left: 0; top: 258px; width: 400px; list-style: none; text-align: center; }
  .benefits li { font-family: "Parisienne", cursive; font-size: 26px; color: var(--green); line-height: 38px; }
  .benefits li span { color: var(--orange); font-family: "Cabin", sans-serif; font-size: 18px; }
  .photo-food {
    position: absolute; left: 22px; top: 577px; width: 354px; height: 235px;
    background: radial-gradient(ellipse at 45% 60%, #6e9b3a 0%, #b9402e 40%, #e9e6e0 75%, #6b4a3a 100%);
    border: 4px solid var(--white);
  }

  /* middle panel */
  .panel--formula { background: linear-gradient(180deg, var(--mint) 0%, var(--mint-deep) 100%); }
  .photo-family {
    position: absolute; left: 31px; top: 28px; width: 340px; height: 236px;
    background: linear-gradient(180deg, #c98a2e 0%, #8f6a2f 45%, #3b3a3a 100%);
    border: 4px solid var(--white);
  }
  .formula-band { position: absolute; left: 0; top: 292px; width: 400px; height: 150px; background: var(--veil); text-align: center; }
  .formula-line { margin-top: 14px; font-size: 17px; font-weight: 500; }
  .formula-line .accent { color: var(--orange); }
  .formula-equals { font-size: 40px; color: var(--orange); line-height: 40px; margin-top: 2px; font-weight: 400; }
  .formula-result { font-family: "Parisienne", cursive; font-size: 42px; color: var(--orange); line-height: 50px; }
  .photo-sport {
    position: absolute; left: 90px; top: 473px; width: 219px; height: 353px;
    background: linear-gradient(180deg, #7a4a3c 0%, #2c4fa0 45%, #5a8e3a 75%, #4d7d31 100%);
    border: 4px solid var(--white);
  }

  /* right panel */
  .panel--offer { background: linear-gradient(180deg, var(--peach) 0%, #fbc374 55%, var(--peach-deep) 100%); }
  .challenge { position: absolute; left: 0; top: 12px; width: 400px; text-align: center; }
  .challenge-title { font-size: 26px; color: var(--orange); line-height: 36px; }
  .challenge-line { font-size: 21px; color: var(--green); line-height: 32px; }
  .photo-beach {
    position: absolute; left: 69px; top: 134px; width: 264px; height: 135px;
    background: linear-gradient(180deg, #a9c2cc 0%, #7d9fb0 60%, #bfb3a0 100%);
    border: 5px solid var(--orange-deep);
  }
  .offer-title { position: absolute; left: 0; top: 290px; width: 400px; text-align: center; font-size: 32px; font-weight: 700; letter-spacing: 0.5px; }
  .offer-box { position: absolute; left: 16px; top: 338px; width: 374px; height: 242px; background: var(--veil); padding: 8px 10px; }
  .offer-list { list-style: none; font-size: 17.5px; line-height: 24.5px; }
  .offer-list b { font-weight: 700; }
  .brand-foot {
    position: absolute; left: 17px; top: 618px; width: 359px; height: 102px;
    background: var(--veil); display: flex; align-items: center; padding-left: 14px; gap: 10px;
  }
  .brand-foot .brand-dot { width: 56px; height: 56px; }
  .brand-foot .brand-name { font-size: 24px; }
  .brand-foot .brand-tag { font-size: 7.5px; }
  .contact { position: absolute; left: 16px; top: 750px; width: 374px; height: 83px; background: var(--veil); padding: 8px 12px; font-size: 17px; line-height: 22px; }
  .contact b { font-weight: 700; }
  .contact .web { color: var(--navy); font-weight: 700; }
</style>
</head>
<body>
<main class="flyer">

  <section class="panel panel--intro">
    <header class="brand-head">
      <span class="brand-dot"></span>
      <div>
        <div class="brand-name">Larkmosstideglow</div>
        <div class="brand-tag">BALANCED NUTRITION, MIND, AND FITNESS</div>
      </div>
    </header>
    <svg class="motto" viewBox="0 0 400 70" aria-hidden="false">
      <path id="motto-curve" d="M14 52 Q200 38 392 20" fill="none"/>
      <text><textPath href="#motto-curve">Everyone deserves true happiness.</textPath></text>
    </svg>
    <h2 class="answer-title"><span class="accent">Real Food</span> is the answer to:</h2>
    <ul class="benefits">
      <li><span>-</span> A body you love <span>-</span></li>
      <li><span>-</span> Reverting illnesses <span>-</span></li>
      <li><span>-</span> Healthy digestion <span>-</span></li>
      <li><span>-</span> Stable blood sugar <span>-</span></li>
      <li><span>-</span> Emotions in control <span>-</span></li>
      <li><span>-</span> Blasting energy <span>-</span></li>
      <li><span>-</span> Sound sleep <span>-</span></li>
    </ul>
    <div class="photo-food" role="img" aria-label="Photo of a fresh mixed salad with tomatoes, greens and olives on a white plate"></div>
  </section>

  <section class="panel panel--formula">
    <div class="photo-family" role="img" aria-label="Photo of a family of four sitting on a park bench in autumn"></div>
    <div class="formula-band">
      <p class="formula-line"><span class="accent">Real Food</span> + water + exercise + L.O.L.</p>
      <p class="formula-equals">=</p>
      <p class="formula-result">“High quality life“</p>
    </div>
    <div class="photo-sport" role="img" aria-label="Photo of a man in a blue football kit kicking a ball on a pitch"></div>
  </section>

  <section class="panel panel--offer">
    <div class="challenge">
      <p class="challenge-title">EASY, right?</p>
      <p class="challenge-line">Challenging: certainly</p>
      <p class="challenge-line">Changing habits: reluctance in sight!</p>
    </div>
    <div class="photo-beach" role="img" aria-label="Photo of a woman walking a dog along a lakeside beach"></div>
    <h2 class="offer-title">WE’RE HERE TO:</h2>
    <div class="offer-box">
      <ol class="offer-list">
        <li>1.&nbsp; Study <b>YOUR</b> unique body composition, food cravings, blockages, illnesses, and personality!</li>
        <li>2.&nbsp; Educate – guide – develop plan – and follow you up 24/7.</li>
        <li>3.&nbsp; You will: taste new food, plan meals, groceries shopping.</li>
        <li>4.&nbsp; You’ll attend: meditation, cooking, and fitness classes.</li>
        <li>5.&nbsp; You’ll make new friends.</li>
      </ol>
    </div>
    <div class="brand-foot">
      <span class="brand-dot"></span>
      <div>
        <div class="brand-name">Larkmosstideglow</div>
        <div class="brand-tag">BALANCED NUTRITION, MIND, AND FITNESS</div>
      </div>
    </div>
    <address class="contact" style="font-style:normal">
      Phone: <b>(555) 010-4821</b><br>
      E-mail:&nbsp; <b>nora@larkmosstideglow.net</b><br>
      <span class="web">www.larkmosstideglow.net</span>
    </address>
  </section>

</main>
</body>
</html>
```